Customizable Gift Note Card Design

I need a gift note card designed for my Healthy Snacks Care Package company. I need to be able to customize each card with the customer's gift message to the recipient and print to a standard printer.

The card should be single-sided 5 x 7, include our logo, keep colors and graphics simple since they will be printed for each individual order on a standard printer. I would like the following quote to be included in a small and subtle way: "Food is symbolic of love when words are inadequate." —Bertram K. Osslund. Our website thebrightpantrybites.example should also be included.

I have included pictures of our product packaging for reference.

Target Market(s)

Gift recipients: Students, people recovering from illness, housewarming, thank you gifts...etc.

Industry/Entity Type

It Company

Colors

Designer to choose colors to be used in the design.

Requirements
Must have
• We are looking for a simple, cute and elegant gift card that reflects our branding. Must be customizable and printable on a standard printer.
• Must be single-sided 5x7.

```html
<!DOCTYPE html>
<html lang="en">
<head>
<meta charset="utf-8">
<title>Gift Note Tag – The Bright Pantry Bites</title>
<link href="https://fonts.googleapis.com/css2?family=Lobster&family=Cousine&display=swap" rel="stylesheet">
<style>
  :root {
    --page: #ffffff;
    --kraft: #b9a077;
    --ink: #0d0a08;
    --ink-soft: #2a2216;
    --ink-muted: #4a3d2a;
    --rule: rgba(42, 34, 22, 0.35);
    --accent: #7a1d1d;
    --eyelet: #7c8a93;
    --eyelet-rim: #c7d1d6;
  }
  html, body {
    margin: 0;
    padding: 0;
    width: 1200px;
    height: 1186px;
    overflow: hidden;
    background: var(--page);
  }
  .tag {
    position: absolute;
    left: 370px;
    top: 103px;
    width: 489px;
    height: 873px;
    background: var(--kraft);
    clip-path: polygon(103px 0, 385px 0, 489px 101px, 489px 873px, 0 873px, 0 101px);
  }
  .tag__eyelet {
    position: absolute;
    left: 198px;
    top: 80px;
    width: 76px;
    height: 76px;
  }
  .tag__emblem {
    position: absolute;
    left: 150px;
    top: 190px;
    width: 172px;
    height: 246px;
    border-radius: 34px;
    background: linear-gradient(180deg, #1a1310 0%, #3a1c1a 55%, #1a1310 100%);
    opacity: 0.85;
  }
  .tag__message {
    position: absolute;
    left: 56px;
    right: 56px;
    top: 470px;
    height: 176px;
    display: flex;
    flex-direction: column;
    justify-content: space-between;
  }
  .tag__message-line {
    display: block;
    height: 0;
    border-bottom: 1px solid var(--rule);
  }
  .tag__quote {
    position: absolute;
    left: 0;
    right: 0;
    top: 680px;
    margin: 0;
    text-align: center;
    font-family: "Lobster", cursive;
    font-weight: 400;
    font-size: 20px;
    line-height: 28px;
    color: var(--ink-muted);
  }
  .tag__author {
    position: absolute;
    right: 70px;
    top: 740px;
    margin: 0;
    font-family: "Lobster", cursive;
    font-size: 17px;
    line-height: 24px;
    color: var(--ink-muted);
  }
  .tag__website {
    position: absolute;
    left: 0;
    right: 0;
    top: 805px;
    margin: 0;
    text-align: center;
    font-family: "Cousine", monospace;
    font-size: 18px;
    line-height: 26px;
    color: var(--accent);
  }
</style>
</head>
<body>
  <main class="tag">
    <svg class="tag__eyelet" viewBox="0 0 76 76" aria-hidden="true">
      <circle cx="38" cy="38" r="37" fill="var(--eyelet)"/>
      <circle cx="38" cy="38" r="29" fill="var(--eyelet-rim)"/>
      <circle cx="38" cy="38" r="18" fill="var(--page)"/>
    </svg>
    <div class="tag__emblem" role="img" aria-label="Illustration of a dapper gentleman: bowler hat, red glasses, moustache and bow tie"></div>
    <div class="tag__message" aria-label="Space for the gift message">
      <span class="tag__message-line"></span>
      <span class="tag__message-line"></span>
      <span class="tag__message-line"></span>
      <span class="tag__message-line"></span>
    </div>
    <p class="tag__quote">Food is symbolic of love when<br>words are inadequate.</p>
    <p class="tag__author">Bertram K. Osslund</p>
    <p class="tag__website">www.thebrightpantrybites.example</p>
  </main>
</body>
</html>
```